Online ticketing company needs new biz card design

Needing an updated business card to reflect our company, incorporating our existing logo and colour scheme (red, black, white). The design should communicate our modern, online, technology, innovation based company.

Details for card need to include the following:

Name
Position
Telephone and extension number
Mobile number
Email
Web address
Physical and/or postal address

Industry/Entity Type

Business

Font styles to use
Sans Serif

Requirements
Must have
• Clear, bold, eye catching design

```html
<!DOCTYPE html>
<html lang="en">
<head>
<meta charset="utf-8">
<title>Tixora Business Card</title>
<link href="https://fonts.googleapis.com/css2?family=Roboto:wght@400;700;900&display=swap" rel="stylesheet">
<style>
  :root {
    --stage: #ecebea;
    --red: #d8222a;
    --red-deep: #8e1016;
    --red-light: #f6c9c9;
    --ink: #111111;
    --paper: #ffffff;
    --ghost: #e3e3e3;
  }
  * { margin: 0; padding: 0; box-sizing: border-box; }
  html, body {
    width: 1200px; height: 784px; overflow: hidden;
    background: var(--stage);
    font-family: "Roboto", Arial, sans-serif;
  }
  .stage { position: relative; width: 1200px; height: 784px; }
  .card {
    position: absolute;
    width: 560px; height: 320px;
    top: 232px;
    overflow: hidden;
    box-shadow: 0 6px 18px rgba(0,0,0,0.18);
  }
  .card-front { left: 30px; }
  .card-back { left: 610px; background: var(--paper); }

  .front-art {
    position: absolute; inset: 0;
    background:
      radial-gradient(ellipse at 70% 30%, rgba(255,255,255,0.75), rgba(255,255,255,0) 55%),
      linear-gradient(100deg, var(--red-deep) 0%, var(--red) 45%, var(--red-light) 100%);
  }
  .front-brand {
    position: absolute; left: 330px; top: 118px;
    width: 200px; height: 70px;
    background: var(--paper);
    display: flex; align-items: center; justify-content: center;
    font-weight: 900; font-size: 42px; letter-spacing: 1px;
    color: var(--red);
  }

  .holder { position: absolute; right: 30px; top: 24px; text-align: right; }
  .holder-name { font-weight: 700; font-size: 17px; color: var(--red); }
  .holder-role { font-size: 12px; color: var(--ink); margin-top: 3px; }

  .brand {
    position: absolute; left: 40px; top: 74px;
    font-weight: 900; font-size: 46px; letter-spacing: 1px;
    color: var(--ink);
  }
  .brand-ghost {
    position: absolute; left: 330px; top: 118px;
    font-weight: 900; font-size: 84px; letter-spacing: 2px;
    color: var(--ghost); white-space: nowrap;
  }

  .contact-list {
    position: absolute; left: 40px; top: 176px;
    list-style: none;
    font-size: 15px; color: var(--ink); line-height: 21px;
  }
  .contact-list li { display: flex; align-items: center; gap: 8px; }
  .contact-list .indent { padding-left: 22px; }
  .icon { width: 14px; height: 14px; fill: var(--red); flex: none; }
</style>
</head>
<body>
<main class="stage">
  <section class="card card-front">
    <div class="front-art" role="img" aria-label="Red gradient background with a grid of squares and flowing wave lines"></div>
    <div class="front-brand">TIXORA</div>
  </section>

  <section class="card card-back">
    <div class="brand-ghost">TIXORA</div>
    <div class="holder">
      <div class="holder-name">Dana Whitlow</div>
      <div class="holder-role">Manager</div>
    </div>
    <div class="brand">TIXORA</div>
    <ul class="contact-list">
      <li>
        <svg class="icon" viewBox="0 0 16 16"><path d="M3 1h3l1.5 4-2 1.3a9 9 0 0 0 4.2 4.2L11 8.5l4 1.5v3a2 2 0 0 1-2 2A12 12 0 0 1 1 3a2 2 0 0 1 2-2z"/></svg>
        555.210.4477 Ext 312
      </li>
      <li>
        <svg class="icon" viewBox="0 0 16 16"><path d="M4 0h8a1 1 0 0 1 1 1v14a1 1 0 0 1-1 1H4a1 1 0 0 1-1-1V1a1 1 0 0 1 1-1zm1 2v10h6V2zm3 11a1 1 0 1 0 0 2 1 1 0 0 0 0-2z"/></svg>
        555.318.9022
      </li>
      <li>
        <svg class="icon" viewBox="0 0 16 16"><path d="M8 0a8 8 0 1 0 0 16A8 8 0 0 0 8 0zm0 1.5c.8 0 1.8 1.9 2.1 5.5H5.9C6.2 3.4 7.2 1.5 8 1.5zM1.6 9h2.8a14 14 0 0 0 .8 4.6A6.5 6.5 0 0 1 1.6 9zm0-2a6.5 6.5 0 0 1 3.6-4.6A14 14 0 0 0 4.4 7zm4.3 2h4.2c-.3 3.6-1.3 5.5-2.1 5.5S6.2 12.6 5.9 9zm4.9 4.6a14 14 0 0 0 .8-4.6h2.8a6.5 6.5 0 0 1-3.6 4.6zM11.6 7a14 14 0 0 0-.8-4.6A6.5 6.5 0 0 1 14.4 7z"/></svg>
        www.tixora.com
      </li>
      <li>
        <svg class="icon" viewBox="0 0 16 16"><path d="M0 3h16v10H0zm1.5 1.5v.4L8 9l6.5-4.1v-.4zM1.5 6.6v4.9h13V6.6L8 10.7z"/></svg>
        info@tixora.com
      </li>
      <li>
        <svg class="icon" viewBox="0 0 16 16"><path d="M8 1 0 8h2v7h4.5v-4.5h3V15H14V8h2z"/></svg>
        1450 Maple Crest Lane
      </li>
      <li class="indent">Fairview, GA 30012</li>
    </ul>
  </section>
</main>
</body>
</html>
```